Clean Plinth Ads Banner Design For A Finance Company

Hi,
We're a UK based finance company and are looking for new banner ads to use on the Plinth Display Network.
We want the end product to stand out by using strong, minimal design - ideally starting from a dark theme, although I'm open to ideas.
The copy should read:
'Fast Bridging Loans From 0.39% PM'
Once we have these designs agreed, we are looking to replicate them for other products, changing only the text on each ad - for example, 'commercial mortgage service you can rely on' or 'development finance service you can rely on'.
The colours used on our website are the following:
Black - #040303
Orange - #f79124
White - #ffffff
Grey - #ffffff
Example ads that I like - https://www.brimcastle.com/wp-content/uploads/2021/07/plinth-display-ads-example-2-final.png.webp
2 - https://quendrahub.com/wp-content/uploads/2020/03/fbdd56ba3bd16c7a8debb13a411de786.jpg

```html
<!DOCTYPE html>
<html lang="en">
<head>
<meta charset="utf-8">
<title>Qorvel – Bridging Loan Display Banners</title>
<link rel="stylesheet" href="https://fonts.googleapis.com/css2?family=Poppins:wght@400;600;700&display=swap">
<style>
  :root {
    --page-bg: #e3dfe0;
    --ink-dark: #1c1d21;
    --brand-orange: #f79124;
    --brand-orange-deep: #d2700f;
    --white: #ffffff;
    --photo-warm: #cdb89c;
    --photo-light: #ece7e0;
    --photo-navy: #2e3542;
    --scale: 1.1811;
  }
  * { box-sizing: border-box; margin: 0; padding: 0; }
  html, body {
    width: 1200px; height: 879px; overflow: hidden;
    background: var(--page-bg);
    font-family: "Poppins", sans-serif;
  }
  .board {
    position: relative;
    width: 1016px; height: 744px;
    transform: scale(var(--scale));
    transform-origin: 0 0;
  }
  .banner {
    position: absolute;
    overflow: hidden;
    background: var(--ink-dark);
    box-shadow: 0 6px 18px rgba(0,0,0,0.12);
  }
  .banner--skyscraper { left: 64px; top: 72px; width: 300px; height: 600px; }
  .banner--narrow { left: 408px; top: 72px; width: 160px; height: 600px; }
  .banner--rectangle { left: 616px; top: 72px; width: 336px; height: 280px; }
  .banner__art { position: absolute; inset: 0; width: 100%; height: 100%; display: block; }
  .banner__copy { position: absolute; left: 0; right: 0; top: 0; bottom: 0; color: var(--white); }
  .banner__copy > * { position: absolute; white-space: nowrap; }
  .brand-name {
    top: 11px;
    font-weight: 700; font-size: 34px; line-height: 40px;
    color: var(--brand-orange); letter-spacing: -0.5px;
  }
  .headline {
    top: 104px;
    font-weight: 700; font-size: 16.5px; line-height: 25px;
  }
  .rating {
    top: 165px;
    font-size: 11px; line-height: 16px; letter-spacing: 1px;
    color: var(--brand-orange);
  }
  .subline {
    top: 188px;
    font-weight: 400; font-size: 14.5px; line-height: 20px;
  }
  .banner--skyscraper .banner__copy > * { left: 0; right: 0; text-align: center; }
  .banner--narrow .banner__copy > *,
  .banner--rectangle .banner__copy > * { left: 16px; right: 8px; text-align: left; }
  .banner--narrow .headline,
  .banner--rectangle .headline { top: 85px; }
  .banner--rectangle .headline,
  .banner--rectangle .rating,
  .banner--rectangle .subline { left: 22px; }
</style>
</head>
<body>
<main class="board">

  <section class="banner banner--skyscraper">
    <svg class="banner__art" viewBox="0 0 300 600">
      <defs>
        <linearGradient id="bg-tower-a" x1="0" y1="0" x2="1" y2="1">
          <stop offset="0" stop-color="#26282d"/><stop offset="1" stop-color="#17181b"/>
        </linearGradient>
        <linearGradient id="photo-a" x1="0" y1="0" x2="1" y2="1">
          <stop offset="0" stop-color="#cdb89c"/><stop offset="0.5" stop-color="#ece7e0"/><stop offset="1" stop-color="#2e3542"/>
        </linearGradient>
      </defs>
      <rect width="300" height="600" fill="url(#bg-tower-a)" role="img" aria-label="Dark photo of office tower glass facades"/>
      <circle cx="40" cy="350" r="110" fill="var(--brand-orange-deep)"/>
      <circle cx="300" cy="370" r="160" fill="var(--white)"/>
      <circle cx="151" cy="530" r="205" fill="var(--brand-orange)"/>
      <circle cx="151" cy="530" r="157" fill="url(#photo-a)" role="img" aria-label="Photo of two colleagues smiling while working at a laptop"/>
    </svg>
    <div class="banner__copy">
      <p class="brand-name">Qorvel</p>
      <h2 class="headline">Bridging Loan Service<br>You Can Rely On</h2>
      <p class="rating" aria-label="Five star rating">★★★★★</p>
      <p class="subline">Rated Service &amp; No<br>Broker Fees</p>
    </div>
  </section>

  <section class="banner banner--narrow">
    <svg class="banner__art" viewBox="0 0 160 600">
      <defs>
        <linearGradient id="bg-tower-b" x1="0" y1="0" x2="1" y2="1">
          <stop offset="0" stop-color="#26282d"/><stop offset="1" stop-color="#17181b"/>
        </linearGradient>
        <linearGradient id="photo-b" x1="0" y1="0" x2="1" y2="1">
          <stop offset="0" stop-color="#cdb89c"/><stop offset="0.5" stop-color="#ece7e0"/><stop offset="1" stop-color="#2e3542"/>
        </linearGradient>
      </defs>
      <rect width="160" height="600" fill="url(#bg-tower-b)" role="img" aria-label="Dark photo of office tower glass facades"/>
      <circle cx="20" cy="370" r="85" fill="var(--brand-orange-deep)"/>
      <circle cx="160" cy="360" r="98" fill="var(--white)"/>
      <circle cx="80" cy="501" r="158" fill="var(--brand-orange)"/>
      <circle cx="80" cy="501" r="120" fill="url(#photo-b)" role="img" aria-label="Photo of two colleagues smiling while working at a laptop"/>
    </svg>
    <div class="banner__copy">
      <p class="brand-name">Qorvel</p>
      <h2 class="headline">Bridging Loan<br>Service You<br>Can Rely On</h2>
      <p class="rating" aria-label="Five star rating">★★★★★</p>
      <p class="subline">Rated Service<br>&amp; No Broker Fees</p>
    </div>
  </section>

  <section class="banner banner--rectangle">
    <svg class="banner__art" viewBox="0 0 336 280">
      <defs>
        <linearGradient id="bg-tower-c" x1="0" y1="0" x2="1" y2="1">
          <stop offset="0" stop-color="#26282d"/><stop offset="1" stop-color="#17181b"/>
        </linearGradient>
        <linearGradient id="photo-c" x1="0" y1="0" x2="1" y2="1">
          <stop offset="0" stop-color="#cdb89c"/><stop offset="0.5" stop-color="#ece7e0"/><stop offset="1" stop-color="#2e3542"/>
        </linearGradient>
      </defs>
      <rect width="336" height="280" fill="url(#bg-tower-c)" role="img" aria-label="Dark photo of office tower glass facades"/>
      <circle cx="340" cy="-10" r="125" fill="var(--white)"/>
      <circle cx="190" cy="380" r="140" fill="var(--white)"/>
      <circle cx="318" cy="235" r="160" fill="var(--brand-orange)"/>
      <circle cx="318" cy="240" r="146" fill="url(#photo-c)" role="img" aria-label="Photo of two colleagues smiling while working at a laptop"/>
    </svg>
    <div class="banner__copy">
      <p class="brand-name">Qorvel</p>
      <h2 class="headline">Bridging Loan<br>Service You<br>Can Rely On</h2>
      <p class="rating" aria-label="Five star rating">★★★★★</p>
      <p class="subline">Rated Service<br>&amp; No Broker Fees</p>
    </div>
  </section>

</main>
</body>
</html>
```